Instructions for nurses on how to give a report on each shift

I have a 2-page reference sheet that needs to be updated to look more aesthetically pleasing.

Target Market(s)

Healthcare, nurses

Industry/Entity Type

Healthcare

Font styles to use
Sans Serif

Requirements
Must have
• Please make sure it is easy to read, the content is well organized and has a flow to it. Please also pick colors that would coordinate with our website www.brivolen.org (so mainly navy and white or off-white with accent colors.) Please make sure to add accent colors to break up the content. The MORVY name and title at the top should remain on the page but I'm not married to the star or logo style. You can do what you think looks best there. Way at the bottom in fine print, I would like for you to add BRIVOLEN © 2019 All rights reserved.

```html
<!DOCTYPE html>
<html lang="en">
<head>
<meta charset="utf-8">
<title>MORVY – Shift Report Huddle</title>
<link rel="stylesheet" href="https://fonts.googleapis.com/css2?family=Open+Sans:ital,wght@0,400;0,600;0,700;1,700&display=swap">
<style>
  :root {
    --navy: #0f3a5f;
    --navy-dark: #0c3558;
    --teal: #1aa7c6;
    --teal-soft: #8fd3e2;
    --sky: #6ea3cb;
    --lavender: #a9aed6;
    --slate: #5a6b7a;
    --ink: #2c2c2c;
    --box-line: #8a8a8a;
    --footer: #d3e3ef;
    --paper: #ffffff;
  }
  * { box-sizing: border-box; margin: 0; padding: 0; }
  html, body { width: 1200px; height: 927px; overflow: hidden; background: var(--paper); }
  body { position: relative; font-family: "Open Sans", Arial, sans-serif; color: var(--ink); }

  .top-band { position: absolute; left: 0; top: 0; width: 1200px; height: 34px; background: var(--navy-dark); }
  .top-stripe { position: absolute; left: 0; top: 34px; width: 1200px; height: 6px; background: var(--teal); }

  .brand { position: absolute; left: 0; top: 62px; width: 1200px; text-align: center; }
  .brand-name { font-weight: 700; font-size: 44px; line-height: 1; color: var(--navy); letter-spacing: 3px; }
  .brand-title { margin-top: 12px; font-weight: 400; font-size: 14px; line-height: 1.2; color: var(--slate); letter-spacing: 0.3px; }

  .motto { position: absolute; left: 174px; top: 167px; width: 849px; height: 88px; border: 1.5px solid var(--teal-soft); display: flex; align-items: center; justify-content: center; text-align: center; }
  .motto p { font-weight: 700; font-style: italic; font-size: 21px; line-height: 1.25; color: var(--navy); }

  .panel { position: absolute; border: 1.5px solid var(--navy); padding: 22px 18px 0 16px; }
  .panel.accent { border-color: var(--teal); padding-left: 27px; }
  .panel.tips { border-color: var(--lavender); }
  .tab { position: absolute; left: -1px; top: -11px; height: 24px; padding: 0 16px; display: flex; align-items: center; font-weight: 700; font-size: 14px; letter-spacing: 0.3px; color: #fff; background: var(--navy); }
  .panel.accent .tab { left: 9px; width: 135px; background: var(--teal); }
  .panel.tips .tab { left: 9px; width: 136px; background: var(--sky); }

  .checklist { list-style: none; }
  .checklist li { position: relative; padding-left: 21px; font-size: 13.2px; line-height: 19px; margin-bottom: 2px; }
  .checklist li::before { content: ""; position: absolute; left: 0; top: 3px; width: 11px; height: 11px; border: 1px solid var(--box-line); }

  .objectives { left: 185px; top: 292px; width: 383px; height: 149px; }
  .outcomes { left: 632px; top: 292px; width: 391px; height: 140px; }
  .who { left: 185px; top: 473px; width: 383px; height: 160px; }
  .when { left: 632px; top: 460px; width: 391px; height: 79px; }
  .where { left: 632px; top: 571px; width: 391px; height: 62px; }
  .tips { left: 176px; top: 662px; width: 847px; height: 176px; padding-left: 28px; display: flex; gap: 114px; }
  .tips .checklist { width: 340px; }
  .tips .checklist:last-child { width: 350px; }
  .tips .checklist li { line-height: 15.5px; margin-bottom: 7px; }

  .footer { position: absolute; left: 0; top: 894px; width: 1200px; height: 33px; background: var(--footer); display: flex; align-items: center; justify-content: center; font-size: 12px; color: var(--ink); }
</style>
</head>
<body>
  <div class="top-band"></div>
  <div class="top-stripe"></div>

  <header class="brand">
    <div class="brand-name">MORVY</div>
    <div class="brand-title">Unit Huddle Reference for Every Shift</div>
  </header>

  <div class="motto">
    <p>When “I” is replaced by “WE”<br>Even illness becomes wellness.</p>
  </div>

  <section class="panel objectives">
    <h2 class="tab">OBJECTIVES:</h2>
    <ul class="checklist">
      <li>Accountability: Declare roles and assignments</li>
      <li>Advocacy: Identify patient needs Transfers</li>
      <li>Critical Thinking: Prioritize and recognize obstacles</li>
      <li>Communication: Share important information</li>
      <li>Collaboration: Utilize an interdisciplinary&nbsp; approach</li>
    </ul>
  </section>

  <section class="panel accent outcomes">
    <h2 class="tab">OUTCOMES:</h2>
    <ul class="checklist">
      <li>Share best practices</li>
      <li>Improve communication</li>
      <li>Promote cohesiveness</li>
      <li>Increase staff morale</li>
      <li>Enhance patient and organizational outcomes</li>
    </ul>
  </section>

  <section class="panel who">
    <h2 class="tab">WHO:</h2>
    <ul class="checklist">
      <li>All nurses on the unit</li>
      <li>All nursing support staff (CNA/MA/HCT)</li>
      <li>Administrator</li>
      <li>Director of Nursing</li>
      <li>Head of pertinent disciplines (Dietary, Social Work, Physical Therapy, Engineering, Central Supply, etc.)</li>
    </ul>
  </section>

  <section class="panel accent when">
    <h2 class="tab">WHEN:</h2>
    <ul class="checklist">
      <li>Every morning (assign&nbsp; a meeting time for each unit )</li>
      <li>Keep meetings within 15 minutes in length</li>
    </ul>
  </section>

  <section class="panel accent where">
    <h2 class="tab">WHERE:</h2>
    <ul class="checklist">
      <li>Nursing station on each unit</li>
    </ul>
  </section>

  <section class="panel tips">
    <h2 class="tab">HELPFUL TIPS:</h2>
    <ul class="checklist">
      <li>Assign a meeting facilitator (usually the administrator of the facility)</li>
      <li>Standing during meetings keeps the meetings short and to the point</li>
      <li>Keeping meetings within 15 minutes emphasizes being prepared and direct</li>
      <li>Keep meeting times consistent (morning is best)</li>
    </ul>
    <ul class="checklist">
      <li>Do not begin until everyone is present (minimizes stragglers)</li>
      <li>Avoid discussing personal concerns</li>
      <li>Include reminders for in-services, meetings, etc. and updates towards the end of the meeting</li>
      <li>Always conclude with achievements, milestones, praise, words of encouragement, motivational quote, etc.</li>
    </ul>
  </section>

  <footer class="footer">BRIVOLEN © 2019 All rights reserved.</footer>
</body>
</html>
```